Harlune Painting

Need business card design

Target Market(s)

Paint

Industry/Entity Type

Painting

Requirements
Must have
• Brice Halvorn | Superviser
| HarLune Painting
| mobile: (360) 555-0148
| email: Brice@harluneinc.example
| site: www.harluneinc.example
| address: 718 Corliss Rd NE Ste 300, Olympia, WA 98501

```html
<!DOCTYPE html>
<html lang="en">
<head>
<meta charset="utf-8">
<title>Harlune Painting – Business Card</title>
<link rel="stylesheet" href="https://fonts.googleapis.com/css2?family=Cinzel:wght@700&family=Arimo:wght@400&display=swap">
<style>
  :root {
    --navy: #223f82;
    --green: #63bb45;
    --white: #ffffff;
    --backdrop: #d6d6d6;
    --ink-light: #ffffff;
  }
  * { margin: 0; padding: 0; box-sizing: border-box; }
  html, body {
    width: 1200px; height: 852px; overflow: hidden;
    background: var(--backdrop);
  }
  .canvas {
    width: 1200px; height: 852px;
    display: flex; flex-direction: column; align-items: center; justify-content: center;
    gap: 30px;
  }
  .card {
    position: relative;
    width: 665px; height: 380px;
    border-radius: 22px;
    overflow: hidden;
    box-shadow: 0 6px 16px rgba(0,0,0,0.22);
  }
  .card-front {
    background: var(--navy);
    display: flex; align-items: center; justify-content: center;
  }
  .brand {
    display: flex; align-items: center; gap: 14px;
    font-family: "Cinzel", serif; font-weight: 700;
    letter-spacing: 0.04em;
  }
  .brand-mark {
    width: 22px; height: 22px; border-radius: 50%;
    background: var(--green);
  }
  .card-front .brand-name { color: var(--white); font-size: 40px; }
  .card-back { background: var(--white); }
  .card-back .wave { position: absolute; inset: 0; }
  .card-back .brand {
    position: absolute; top: 52px; right: 38px; gap: 10px;
  }
  .card-back .brand-name { color: var(--navy); font-size: 24px; }
  .card-back .brand-mark { width: 14px; height: 14px; }
  .address {
    position: absolute; right: 40px; top: 190px;
    font-family: "Arimo", sans-serif; font-size: 15px; line-height: 1.35;
    color: var(--ink-light); text-align: right;
  }
  .person {
    position: absolute; left: 40px; top: 262px;
    font-family: "Arimo", sans-serif; color: var(--ink-light);
  }
  .person-name {
    font-family: "Cinzel", serif; font-weight: 700;
    color: var(--green); font-size: 21px; letter-spacing: 0.02em; line-height: 1.1;
  }
  .person-title { font-size: 15px; margin-bottom: 10px; }
  .contact-list { list-style: none; font-size: 15px; line-height: 1.45; }
  .contact-list li { display: flex; align-items: center; gap: 8px; }
  .contact-list svg { width: 12px; height: 12px; flex: none; }
</style>
</head>
<body>
<main class="canvas">
  <section class="card card-front" aria-label="Card front">
    <div class="brand">
      <span class="brand-mark"></span>
      <span class="brand-name">Harlune Painting</span>
    </div>
  </section>

  <section class="card card-back" aria-label="Card back">
    <svg class="wave" viewBox="0 0 665 380" preserveAspectRatio="none" aria-hidden="true">
      <path d="M0,262 C120,182 300,170 430,166 C540,162 620,128 665,78 L665,380 L0,380 Z" fill="var(--navy)"/>
      <path d="M0,250 C120,170 300,158 430,154 C540,150 615,118 660,70" fill="none" stroke="var(--green)" stroke-width="6"/>
    </svg>

    <div class="brand">
      <span class="brand-mark"></span>
      <span class="brand-name">Harlune Painting</span>
    </div>

    <p class="address">718 Corliss Rd NE Ste 300,<br>Olympia, WA 98501</p>

    <div class="person">
      <p class="person-name">BRICE HALVORN</p>
      <p class="person-title">Superviser</p>
      <ul class="contact-list">
        <li>
          <svg viewBox="0 0 12 12"><path d="M2.5 1 L4.5 1 L5.2 3.4 L4 4.4 C4.6 5.8 6.2 7.4 7.6 8 L8.6 6.8 L11 7.5 L11 9.5 C11 10.3 10.3 11 9.5 11 C5 11 1 7 1 2.5 C1 1.7 1.7 1 2.5 1 Z" fill="var(--green)"/></svg>
          (360) 555-0148
        </li>
        <li>
          <svg viewBox="0 0 12 12"><rect x="0.5" y="2" width="11" height="8" fill="var(--green)"/><path d="M0.5 2 L6 6.5 L11.5 2" fill="none" stroke="var(--navy)" stroke-width="1"/></svg>
          Brice@harluneinc.example
        </li>
        <li>
          <svg viewBox="0 0 12 12"><circle cx="6" cy="6" r="5.5" fill="var(--green)"/><path d="M0.5 6 H11.5 M6 0.5 C3.5 3 3.5 9 6 11.5 M6 0.5 C8.5 3 8.5 9 6 11.5" fill="none" stroke="var(--navy)" stroke-width="0.8"/></svg>
          www.harluneinc.example
        </li>
      </ul>
    </div>
  </section>
</main>
</body>
</html>
```